Need Edgy Web Design Home Page for Entertainment Agency

We need a web design splash page for our entertainment company, Vexa Prime Agency based (Los Angeles and New York).
Vexa Prime is a full service PR, marketing and special events agency based in Los Angeles and New York. We aim to serve the most elite in entertainment, media and sports.

With a combined experience of over 30 years in the entertainment industry, our team is committed to deliver each client with the upmost service and contemporary strategies to increase your business objective.

CREATIVE, EDGY & TRENDSETTING

SERVICES

PR Campaigns

Media Relations

Talent Representation

Brand Marketing & Activations

Special Events: Publicity & Consulting

EXPERTISE

Television

Film

Talent

Music

Marketing & Promotions

Industry Events

Digital & Social Media

Looking for a home page that is flashy, edgy and creative. I've provided our logos and contact details:

Delia Fortunez
dfortunez@kelvoritla.com

Tobias Renn
trenn@kelvoritny.com

Paloma Quiroga
pquiroga@kelvoritla.com

Target Market(s)

Los Angeles and New York

Industry/Entity Type

Entertainment

Number of Pages Required

1 page

Font styles to use
Serif
Decorative

Requirements
Must have
• 1. Logo
• 2. Description of services but done creatively
• 4. Visuals (Stock images: cool edgy millennials & graphics images that make sense for our agency)
• 5. Contact Details
• Reference: https://www.tunelathery.net & http://www.thevolrenagency.com
Nice to have
• If possible would love to have stock cartoon images included as images of Delia and I. Reference image (http://www.pixmerrow.com/pic-482915306/stock-vector-cute-cartoon-characters-young-boy-and-girl-in-cool-casual-outfits.html)
Should not have
• Should not look boring!

```html
<!DOCTYPE html>
<html lang="en">
<head>
<meta charset="utf-8">
<title>Vexa Prime — Home</title>
<link href="https://fonts.googleapis.com/css2?family=Roboto+Condensed:wght@400;700&family=Roboto:wght@400;500&family=Open+Sans:ital,wght@0,400;1,400&display=swap" rel="stylesheet">
<style>
:root{
  --ink:#2d2c31;
  --ink-soft:#3a393f;
  --sun:#fdcf58;
  --gold:#d9a93a;
  --text:#4a4a4a;
  --muted:#666;
  --white:#ffffff;
  --line:#d6d6d6;
}
*{margin:0;padding:0;box-sizing:border-box}
html,body{width:1200px;height:2182px;overflow:hidden}
body{position:relative;background:var(--white);font-family:"Open Sans",sans-serif;color:var(--text)}
.abs{position:absolute}

/* hero */
.hero{left:0;top:0;width:1200px;height:640px;background:var(--ink)}
.brand{left:99px;top:40px;display:flex;align-items:center;gap:14px;font-family:"Roboto Condensed",sans-serif;font-size:36px;color:var(--sun);letter-spacing:1px}
.brand-dot{width:58px;height:58px;border-radius:50%;background:var(--sun)}
.nav{left:428px;top:54px;display:flex;font-family:"Roboto Condensed",sans-serif;font-size:14px;color:var(--white)}
.nav a{color:var(--white);text-decoration:none;margin-right:44px;position:relative}
.nav a.active::after{content:"";position:absolute;left:0;right:0;top:28px;height:2px;background:var(--sun)}
.signup{left:1020px;top:47px;width:82px;height:30px;background:var(--sun);border-radius:3px;font-family:"Roboto Condensed",sans-serif;font-size:12px;color:var(--ink);display:flex;align-items:center;justify-content:center}
.hero-title{left:97px;top:270px;font-family:"Roboto Condensed",sans-serif;font-size:64px;font-weight:700;color:var(--white);letter-spacing:1px;line-height:1}
.hero-text{left:99px;top:346px;width:340px;font-family:"Roboto",sans-serif;font-size:12.5px;line-height:26px;color:var(--white)}
.dots{left:97px;top:441px;display:flex;gap:6px}
.dots span{width:14px;height:14px;border-radius:50%;border:1.5px solid var(--white)}
.dots span.on{background:var(--white)}
.hero-art{left:470px;top:130px;width:600px;height:510px;border-radius:40px 40px 0 0;background:radial-gradient(ellipse at 50% 55%,#4b4a52 0%,#3a393f 60%,transparent 75%)}
.clouds{left:0;top:510px}

/* services */
.services{left:0;top:640px;width:1200px;height:420px;background:var(--sun)}
.h2{font-family:"Roboto Condensed",sans-serif;font-weight:400;color:var(--ink);text-align:center;width:1200px;left:0}
.services-title{top:695px;font-size:29px}
.service{width:230px;text-align:center;top:764px}
.service-icon{width:116px;height:116px;border-radius:50%;background:var(--ink);margin:0 auto;border:3px solid var(--white);display:flex;align-items:center;justify-content:center;box-shadow:0 14px 10px -10px rgba(0,0,0,.18);position:relative}
.service-icon::before{content:"";position:absolute;inset:7px;border-radius:50%;border:1px dashed rgba(255,255,255,.35)}
.service h3{font-family:"Roboto",sans-serif;font-weight:400;font-size:16px;color:var(--ink);margin-top:32px;letter-spacing:.3px}
.service p{font-size:11px;line-height:20px;color:var(--ink);margin-top:8px}

/* welcome */
.welcome-title{top:1100px;font-size:38px;color:#3b3b3b}
.welcome-title em{font-style:normal;color:var(--gold)}
.welcome-text{left:170px;top:1157px;width:860px;text-align:center;font-size:12px;line-height:21px;color:var(--muted)}
.btn{left:538px;top:1241px;width:124px;height:38px;border:1px solid var(--line);border-radius:3px;font-family:"Roboto",sans-serif;font-size:12.5px;color:var(--ink);display:flex;align-items:center;justify-content:center;gap:6px}

/* agency */
.agency{left:0;top:1320px;width:1200px;height:433px;background:var(--sun)}
.video{left:99px;top:1402px;width:451px;height:268px;background:linear-gradient(180deg,#2f5e96 0%,#7a5a78 40%,#e7833a 72%,#1a1a1a 100%)}
.video-play{left:298px;top:1517px;width:52px;height:34px;background:rgba(230,230,230,.85);border-radius:4px}
.video-bar{left:110px;top:1640px;width:430px;height:18px;background:rgba(20,20,20,.8);border-radius:2px}
.agency-title{left:582px;top:1412px;font-family:"Roboto Condensed",sans-serif;font-weight:400;font-size:27px;color:var(--ink)}
.agency-text{left:583px;top:1455px;width:520px;font-size:11px;line-height:20px;color:var(--ink)}
.checks{left:583px;top:1535px;list-style:none;font-size:12px;color:var(--ink)}
.checks li{height:34.5px;display:flex;align-items:flex-start;gap:14px}

/* testimonials */
.say-title{top:1783px;font-size:31px;color:#444;font-family:"Roboto",sans-serif}
.quote{width:430px;top:1862px;border-left:1px solid var(--line);height:170px;padding-left:26px}
.quote p{width:400px;font-style:italic;font-size:13px;line-height:23px;color:var(--muted);padding-top:8px}
.person{display:flex;align-items:center;gap:24px;margin-top:18px}
.avatar{width:76px;height:76px;border-radius:50%;background:linear-gradient(135deg,#c9a98f,#8a6d5c)}
.who{font-style:italic;font-size:13px;line-height:21px;color:var(--gold)}

/* footer */
.footer{left:0;top:2073px;width:1200px;height:109px;background:var(--ink)}
.copy{left:98px;top:2104px;font-family:"Roboto",sans-serif;font-size:12.5px;color:var(--white)}
.foot-links{left:98px;top:2139px;font-family:"Roboto",sans-serif;font-size:12.5px;color:var(--white)}
.social{left:982px;top:2112px;display:flex;gap:6px}
.social span{width:36px;height:36px;border-radius:4px;background:#6a6a70}
.social span:nth-child(2){background:#3aa9e0}
.social span:nth-child(3){background:#2a7ab8}
</style>
</head>
<body>

<section class="hero abs"></section>
<div class="brand abs"><span>Vexa Prime</span><span class="brand-dot"></span></div>
<nav class="nav abs">
  <a class="active">HOME</a><a>ABOUT VEXA PRIME</a><a>OUR SERVICES</a><a>EXPERTISE</a><a>CONTACT US</a>
</nav>
<div class="signup abs">SIGN UP</div>
<h1 class="hero-title abs">VEXA PRIME</h1>
<p class="hero-text abs">Vexa Prime is a full service PR, marketing and special events agency based in Los Angeles and New York. We aim to serve the most elite in entertainment, media and sports.</p>
<div class="dots abs"><span class="on"></span><span></span><span></span></div>
<div class="hero-art abs" role="img" aria-label="Cartoon illustration of young people sharing messages on phones and tablets"></div>

<svg class="clouds abs" width="1200" height="140" viewBox="0 0 1200 140" aria-hidden="true">
  <g fill="#fdcf58">
    <rect x="0" y="95" width="1200" height="45"/>
    <circle cx="40" cy="80" r="45"/><circle cx="110" cy="90" r="36"/><circle cx="175" cy="98" r="30"/>
    <circle cx="240" cy="98" r="33"/><circle cx="300" cy="105" r="26"/><circle cx="355" cy="110" r="22"/>
    <circle cx="410" cy="102" r="30"/><circle cx="470" cy="108" r="24"/><circle cx="530" cy="100" r="32"/>
    <circle cx="600" cy="108" r="24"/><circle cx="660" cy="102" r="30"/><circle cx="720" cy="108" r="24"/>
    <circle cx="780" cy="102" r="30"/><circle cx="840" cy="108" r="22"/><circle cx="900" cy="95" r="32"/>
    <circle cx="965" cy="85" r="38"/><circle cx="1040" cy="72" r="44"/><circle cx="1110" cy="60" r="48"/>
    <circle cx="1180" cy="52" r="50"/>
  </g>
</svg>

<section class="services abs"></section>
<h2 class="h2 services-title abs">OUR SERVICES</h2>

<div class="service abs" style="left:90px">
  <div class="service-icon"><svg width="44" height="44" viewBox="0 0 24 24" fill="#fdcf58"><path d="M3 10h3l9-5v14l-9-5H3z"/><path d="M6 14l1 5h2l-1-5z"/><path d="M17 9h3v2h-3zM17 13h3v2h-3z"/></svg></div>
  <h3>PR CAMPAIGNS</h3>
  <p>Lorem ipsum dolor sit amet, consectetur adipiscing elit, sed do eiusmod tempor incididunt ut labore et dolore</p>
</div>
<div class="service abs" style="left:356px">
  <div class="service-icon"><svg width="40" height="40" viewBox="0 0 24 24" fill="#fdcf58"><rect x="9" y="2" width="6" height="12" rx="3"/><path d="M6 11a6 6 0 0012 0h-2a4 4 0 01-8 0z"/><rect x="11" y="17" width="2" height="4"/><rect x="8" y="20" width="8" height="2"/></svg></div>
  <h3>MEDIA RELATIONS</h3>
  <p>Lorem ipsum dolor sit amet, consectetur adipiscing elit, sed do eiusmod tempor incididunt ut labore et dolore</p>
</div>
<div class="service abs" style="left:621px">
  <div class="service-icon"><svg width="38" height="38" viewBox="0 0 24 24" fill="#fdcf58"><path d="M5 2h10l5 5v15H5z"/><path d="M8 11h9v1.5H8zM8 14h9v1.5H8zM8 17h9v1.5H8z" fill="#2d2c31"/></svg></div>
  <h3>TALENT REPRESENTATION</h3>
  <p>Lorem ipsum dolor sit amet, consectetur adipiscing elit, sed do eiusmod tempor incididunt ut labore et dolore</p>
</div>
<div class="service abs" style="left:881px">
  <div class="service-icon"><svg width="44" height="40" viewBox="0 0 24 22" fill="#fdcf58"><path d="M2 2h1.5v17H22v1.5H2z"/><rect x="6" y="11" width="2.5" height="7"/><rect x="10" y="8" width="2.5" height="10"/><rect x="14" y="12" width="2.5" height="6"/><rect x="18" y="5" width="2.5" height="13"/></svg></div>
  <h3>BRAND MARKETING</h3>
  <p>Lorem ipsum dolor sit amet, consectetur adipiscing elit, sed do eiusmod tempor incididunt ut labore et dolore</p>
</div>

<svg class="abs" style="left:0;top:1030px" width="1200" height="40" viewBox="0 0 1200 40" aria-hidden="true">
  <path d="M0 0H1200V20C1100 8 1000 30 880 22C760 14 680 6 560 16C440 26 340 30 200 14C120 6 60 8 0 18Z" fill="#fdcf58"/>
</svg>

<h2 class="h2 welcome-title abs">WELCOME TO <em>VEXA PRIME</em></h2>
<p class="welcome-text abs">Vexa Prime is a full service PR, marketing and special events agency based in Los Angeles. We aim to serve the most elite in entertainment, media and sports. With a combined experience of over 30 years in the entertainment industry, our team is committed to deliver each client with the upmost service and contemporary strategies to increase your business objective.</p>
<div class="btn abs">READ MORE <svg width="12" height="12" viewBox="0 0 12 12"><circle cx="6" cy="6" r="6" fill="#2d2c31"/><path d="M5 3l3 3-3 3" stroke="#fff" stroke-width="1.6" fill="none"/></svg></div>

<svg class="abs" style="left:0;top:1300px" width="1200" height="40" viewBox="0 0 1200 40" aria-hidden="true">
  <path d="M0 20C120 8 220 6 360 14C500 22 600 26 740 16C860 8 1000 4 1200 18V40H0Z" fill="#fdcf58"/>
</svg>
<section class="agency abs"></section>
<svg class="abs" style="left:0;top:1733px" width="1200" height="40" viewBox="0 0 1200 40" aria-hidden="true">
  <path d="M0 0H1200V8C1080 20 960 26 820 18C680 10 560 4 420 12C280 20 160 26 0 20Z" fill="#fdcf58"/>
</svg>

<div class="video abs" role="img" aria-label="Video still of a city skyline and statue silhouetted against a sunset"></div>
<div class="video-play abs"><svg width="52" height="34" viewBox="0 0 52 34"><path d="M21 10l12 7-12 7z" fill="#333"/></svg></div>
<div class="video-bar abs"><svg width="430" height="18" viewBox="0 0 430 18"><rect x="10" y="7" width="300" height="4" fill="#555"/><rect x="10" y="7" width="130" height="4" fill="#2a9fd8"/><rect x="350" y="5" width="30" height="8" fill="#2a9fd8"/></svg></div>

<h2 class="agency-title abs">PR, MARKETING &amp; SPECIAL EVENTS AGENCY</h2>
<p class="agency-text abs">Lorem ipsum dolor sit amet, consectetur adipiscing elit, sed do eiusmod tempor incididunt ut labore et dolore magna aliqua. Ut enim ad minim veniam, quis nostrud exercitation ullamco laboris Lorem ipsum dolor sit amet, consectetur adipiscing elit,</p>
<ul class="checks abs">
  <li><svg width="13" height="13" viewBox="0 0 12 12"><path d="M1 6l3 3 7-7" stroke="#2d2c31" stroke-width="2.2" fill="none"/></svg>Nemo enim ipsam voluptatem quia</li>
  <li><svg width="13" height="13" viewBox="0 0 12 12"><path d="M1 6l3 3 7-7" stroke="#2d2c31" stroke-width="2.2" fill="none"/></svg>Sed ut perspiciatis unde omnis iste natus</li>
  <li><svg width="13" height="13" viewBox="0 0 12 12"><path d="M1 6l3 3 7-7" stroke="#2d2c31" stroke-width="2.2" fill="none"/></svg>Lorem ipsum dolor sit amet, consectetur</li>
  <li><svg width="13" height="13" viewBox="0 0 12 12"><path d="M1 6l3 3 7-7" stroke="#2d2c31" stroke-width="2.2" fill="none"/></svg>Duis aute irure dolor in reprehenderit</li>
</ul>

<h2 class="h2 say-title abs">WHAT OTHERS SAY ABOUT US</h2>
<div class="quote abs" style="left:131px">
  <p>“ Lorem ipsum dolor sit amet, consectetur adipisicing elit, sed do eiusmod tempor incididunt ut labore et dolore magna aliqua<br>Unde omnis, consequuntur.</p>
  <div class="person"><div class="avatar" role="img" aria-label="Portrait photo of a client"></div><div class="who">JOHN DOE<br>Lumen Grove Studio,</div></div>
</div>
<div class="quote abs" style="left:653px">
  <p>“ Lorem ipsum dolor sit amet, consectetur adipisicing elit, sed do eiusmod tempor incididunt ut labore et dolore magna aliqua<br>Unde omnis, consequuntur.</p>
  <div class="person"><div class="avatar" role="img" aria-label="Portrait photo of a client" style="background:linear-gradient(135deg,#8a7a6c,#3d3430)"></div><div class="who">JOHN DOE<br>Lumen Grove Studio,</div></div>
</div>

<footer class="footer abs"></footer>
<svg class="abs" style="left:0;top:2066px" width="1200" height="10" viewBox="0 0 1200 10" aria-hidden="true">
  <defs><pattern id="zig" width="12" height="10" patternUnits="userSpaceOnUse"><path d="M0 10L6 3L12 10Z" fill="#2d2c31"/></pattern></defs>
  <rect width="1200" height="10" fill="url(#zig)"/>
</svg>
<p class="copy abs">© 2015 Vexa Prime All rights reserved.</p>
<p class="foot-links abs">Home &nbsp;| &nbsp;About Us &nbsp;| &nbsp;Services &nbsp;| &nbsp;24/7 Telephone | Contact Us</p>
<div class="social abs"><span></span><span></span><span></span></div>

</body>
</html>
```